Insert sheet for our Dog Food Package

We need an information sheet to go inn our pet food package, with branding, and information on ingredients, nutrition and feeding guidance. We will also need two additional items which will be a variation on the label design:
1) Label for package (detailed label about us and our food)
2) Label for outer shipping box (simple label for branding)
We will start with the information, insert page. The winning designer will then deliver the package and box labels as simplified versions of the same graphical theme.
I have attached samples of an earlier drafts of the insert piece. Please disregard the style, form and colors of the examples given. THEY ARE ONLY THERE TO SHOW WHAT INFORMATION SHOULD BE INCLUDED. All colors and style should be from our logo (attached). All graphics, font styles, and placement of elements need to be YOUR creative design - not a copy of the sample we gave. PLEASE READ THIS AND PLEASE DO NOT SUBMIT ANY VARIATION OF THE EXAMPLES!!!!!!!

Target Market(s)

Pet Owners

Industry/Entity Type

Pet Food

Colors
EB3D1F
EC4F4E
F09395
F8D3D4
FCEDEE

Requirements
Must have
• All new design. New colors (based in the palette of our logo), new graphics, new fonts, new placement of elements.
Should not have
• Please disregard the style, form and colors of the examples given. THEY ARE ONLY THERE TO SHOW WHAT INFORMATION SHOULD BE INCLUDED.

```html
<!DOCTYPE html>
<html lang="en">
<head>
<meta charset="utf-8">
<title>Brava Insert Sheet – Prepared With Love For Shadow</title>
<link rel="stylesheet" href="https://fonts.googleapis.com/css2?family=Montserrat:wght@400;600;700;800;900&family=Open+Sans:wght@400;600;700&display=swap">
<style>
  :root {
    --brand-red: #b3241c;
    --brand-red-bright: #eb3d1f;
    --brand-coral: #ec4f4e;
    --brand-pink: #f09395;
    --brand-blush: #f8d3d4;
    --brand-mist: #fcedee;
    --ink: #3a3a3a;
    --ink-soft: #666;
    --paper: #ffffff;
    --stage: #ececec;
    --photo-light: #f6f1eb;
    --photo-warm: #e2c7a6;
  }
  * { box-sizing: border-box; margin: 0; padding: 0; }
  html, body { width: 1200px; height: 2400px; overflow: hidden; }
  body { background: var(--stage); font-family: "Open Sans", Arial, sans-serif; color: var(--ink); position: relative; }

  .insert-sheet {
    position: absolute; left: 50px; top: 485px;
    width: 1100px; height: 1430px;
    background: var(--paper);
    overflow: hidden;
    box-shadow: 0 10px 30px rgba(0,0,0,.12);
  }

  /* Hero */
  .hero { position: absolute; left: 0; top: 0; width: 100%; height: 640px; background: var(--brand-red); }
  .brand-card {
    position: absolute; left: 40px; top: 36px; width: 300px; height: 96px;
    background: var(--paper); border-radius: 10px;
    display: flex; align-items: center; gap: 16px; padding: 0 26px;
  }
  .brand-dot { width: 44px; height: 44px; border-radius: 50%; background: var(--brand-red); flex: none; }
  .brand-name { font-family: "Montserrat", Arial, sans-serif; font-weight: 800; font-size: 40px; letter-spacing: 3px; color: var(--brand-red); }

  .headline {
    position: absolute; left: 40px; top: 230px; width: 600px;
    font-family: "Montserrat", Arial, sans-serif; font-weight: 900;
    font-size: 68px; line-height: 1.04; color: var(--paper); text-transform: uppercase;
  }
  .dog-photo {
    position: absolute; right: 40px; top: 40px; width: 420px; height: 600px;
    border-radius: 14px 14px 0 0;
    background: linear-gradient(180deg, var(--photo-light) 0%, var(--photo-warm) 100%);
  }

  .zigzag { position: absolute; left: 0; top: 612px; }

  /* Intro copy */
  .intro { position: absolute; left: 40px; top: 670px; width: 1020px; display: flex; gap: 60px; }
  .intro-col { flex: 1; font-size: 15px; line-height: 1.6; color: var(--ink-soft); }
  .intro-col p + p { margin-top: 12px; }

  /* Info panels */
  .panels { position: absolute; left: 40px; top: 930px; width: 1020px; display: flex; gap: 60px; align-items: stretch; }
  .panel { flex: 1; display: flex; flex-direction: column; }
  .panel-title {
    background: var(--brand-red); color: var(--paper);
    font-family: "Montserrat", Arial, sans-serif; font-weight: 700; font-size: 20px;
    text-align: center; padding: 14px 0; border-radius: 8px 8px 0 0;
  }
  .panel-body { flex: 1; background: var(--brand-mist); padding: 18px 24px 22px; }
  .panel-subtitle {
    font-family: "Montserrat", Arial, sans-serif; font-weight: 600; font-size: 15px;
    letter-spacing: 1px; text-transform: uppercase; color: var(--brand-red);
    text-align: center; padding-bottom: 12px; border-bottom: 2px solid var(--brand-blush); margin-bottom: 14px;
  }
  .nutrients { display: grid; grid-template-columns: 1fr 1fr; gap: 6px 20px; font-weight: 700; font-size: 16px; margin-bottom: 16px; }
  .nutrients span { color: var(--brand-red); }
  .ingredients { font-size: 14px; line-height: 1.6; color: var(--ink-soft); }

  .feeding-table { width: 100%; border-collapse: collapse; font-size: 15px; }
  .feeding-table th {
    font-family: "Montserrat", Arial, sans-serif; font-size: 12px; font-weight: 700;
    text-transform: uppercase; text-align: left; color: var(--ink); padding: 0 6px 8px;
  }
  .feeding-table th:last-child, .feeding-table td:last-child { text-align: right; }
  .feeding-table td { padding: 6px; border-top: 1px solid var(--brand-blush); }
  .feeding-table td:last-child { color: var(--brand-red); font-weight: 700; }

  .grass-strip {
    position: absolute; left: 0; bottom: 0; width: 100%; height: 110px;
    background: linear-gradient(180deg, rgba(255,255,255,0) 0%, #7fb24a 35%, #4f8a2a 100%);
  }
</style>
</head>
<body>
  <main class="insert-sheet">
    <section class="hero">
      <div class="brand-card">
        <span class="brand-dot"></span>
        <span class="brand-name">BRAVA</span>
      </div>
      <h1 class="headline">Prepared<br>with love<br>for Shadow</h1>
      <div class="dog-photo" role="img" aria-label="Photo of a sitting beagle puppy, the dog Shadow"></div>
    </section>

    <svg class="zigzag" width="1100" height="40" viewBox="0 0 1100 40" aria-hidden="true">
      <path d="M0 40 L0 20 L20 8 L40 20 L60 8 L80 20 L100 8 L120 20 L140 8 L160 20 L180 8 L200 20 L220 8 L240 20 L260 8 L280 20 L300 8 L320 20 L340 8 L360 20 L380 8 L400 20 L420 8 L440 20 L460 8 L480 20 L500 8 L520 20 L540 8 L560 20 L580 8 L600 20 L620 8 L640 20 L660 8 L680 20 L700 8 L720 20 L740 8 L760 20 L780 8 L800 20 L820 8 L840 20 L860 8 L880 20 L900 8 L920 20 L940 8 L960 20 L980 8 L1000 20 L1020 8 L1040 20 L1060 8 L1080 20 L1100 8 L1100 40 Z" fill="#ffffff"/>
    </svg>

    <section class="intro">
      <div class="intro-col">
        <p>All of us at Brava are dog people, and we have always treated our dogs as true members of the family.</p>
        <p>Years ago we noticed that the food in our bowls was not as good as it should be, so we began cooking healthy meals at home for our own dogs.</p>
        <p>Over time, friends asked for the same meals, and we learned how much better their dogs felt with real, fresh food.</p>
      </div>
      <div class="intro-col">
        <p>We are proud to offer this great product to your canine friends and invite you to join the Brava Super Food revolution. Shadow's meals use fresh meats, vegetables and whole grains chosen for health.</p>
      </div>
    </section>

    <section class="panels">
      <article class="panel">
        <h2 class="panel-title">We prepared the best for Shadow</h2>
        <div class="panel-body">
          <h3 class="panel-subtitle">Nutritional Information</h3>
          <div class="nutrients">
            <div>Protein: <span>19%</span></div>
            <div>Crude Fiber: <span>3.5%</span></div>
            <div>Total Fat: <span>8.5%</span></div>
            <div>Moisture: <span>72%</span></div>
          </div>
          <p class="ingredients">Potatoes, Chicken, Carrots, Green Beans, Brown Rice, Peas, Fish Oil, Calcium Carbonate, Dicalcium Phosphate, Salt, Zinc Sulfate, Iron Sulfate, Vitamin E, Vitamin B12, Vitamin D3, Riboflavin, Folic Acid.</p>
        </div>
      </article>
      <article class="panel">
        <h2 class="panel-title">How much should I feed Shadow?</h2>
        <div class="panel-body">
          <h3 class="panel-subtitle">Recommended Feeding Plan</h3>
          <table class="feeding-table">
            <thead><tr><th>Approximate weight</th><th>Full meal</th></tr></thead>
            <tbody>
              <tr><td>10 lbs</td><td>250 g</td></tr>
              <tr><td>10 – 20 lbs</td><td>300 g</td></tr>
              <tr><td>20 – 30 lbs</td><td>350 g</td></tr>
              <tr><td>30 – 50 lbs</td><td>400 g</td></tr>
              <tr><td>50 – 70 lbs</td><td>450 g</td></tr>
              <tr><td>70+ lbs</td><td>500 g</td></tr>
            </tbody>
          </table>
        </div>
      </article>
    </section>

    <div class="grass-strip" role="img" aria-label="Photo of green grass along the bottom edge"></div>
  </main>
</body>
</html>
```